Maplewood Surgery Brochure Design

Maplewood Surgery (maplewoodsurgery.example)

Is a comprehensive breast care center that focuses on caring for women with breast cancer and other breast pathologies. We need a promotional and marketing brochure, in a tri-fold format, to provide information about our office and describe the services that we offer.

Deliverable

* The brochure should be completed by August 24th
* We will need the necessary files to get the brochure printed (.ai, .indd, etc).

Target Market(s)

Primarily patients of age between 30+ and 70+. The brochure will also be placed in doctor's waiting room

Industry/Entity Type

Marketing

Requirements
Must have
• * Make use of the color scheme as the website (http://maplewoodsurgery.example, http://maplewoodsurgery.example/static/theme-fuchsia.png)
* Incorporate the following graphic elements:
* The company’s logo (provided as an attachment)
* At least one images from the homepage
* Photos of the primary doctor and her staff
* Map to show the office location and phone number
* Enclose a breast cancer self-exam card (http://maplewoodsurgery.example/static/shower-card.jpg)
* A portion of the brochure must be detachable and serve as business cards that can be cut off (see attachment).
Nice to have
• Here is an example of a brochure that we like:

http://designbazaro.example/item/flexible-trifold-brochure/318274?WT.ac=search_item&WT.seg_1=search_item&WT.z_author=mendavik

```html
<!DOCTYPE html>
<html lang="en">
<head>
<meta charset="utf-8">
<title>Maplewood Surgery – Tri-fold Brochure</title>
<link rel="stylesheet" href="https://fonts.googleapis.com/css2?family=Crimson+Text:wght@400;600;700&family=Great+Vibes&display=swap">
<style>
  :root {
    --canvas: #d6d6d8;
    --paper: #fbe9f0;
    --paper-light: #fdf4f7;
    --paper-warm: #f9e3e6;
    --band: #f3c9dc;
    --magenta: #8a1a55;
    --magenta-deep: #6d1042;
    --rose: #c9548e;
    --rose-soft: #e59cbf;
    --text: #7a1450;
    --map-frame: #8a1a55;
  }
  * { box-sizing: border-box; margin: 0; padding: 0; }
  html, body { width: 1200px; height: 900px; overflow: hidden; }
  body {
    background: var(--canvas);
    font-family: "Crimson Text", Georgia, serif;
    color: var(--text);
    position: relative;
  }
  .brochure {
    position: absolute;
    left: 60px; top: 30px;
    width: 1080px; height: 730px;
    display: flex;
    box-shadow: 0 4px 14px rgba(0,0,0,.18);
  }
  .panel { position: relative; width: 360px; height: 100%; overflow: hidden; }
  .panel--doctor { background: linear-gradient(180deg, var(--paper-light) 0%, var(--paper) 55%, var(--paper-warm) 100%); }
  .panel--contact { background: linear-gradient(180deg, #fbf0f3 0%, #f7e4ec 60%, #fbeef2 100%); border-left: 1px solid #ecd0dc; border-right: 1px solid #ecd0dc; }
  .panel--cover { background: linear-gradient(180deg, #fff 0%, #fbeaf1 55%, var(--paper) 100%); }

  .swoosh { position: absolute; left: 0; width: 100%; }

  /* Doctor panel */
  .doctor-photo {
    position: absolute; left: 90px; top: 55px;
    width: 165px; height: 195px;
    background: linear-gradient(160deg, #3a4a66 0%, #5b4a42 60%, #7c6a5c 100%);
  }
  .doctor-name {
    position: absolute; top: 268px; width: 100%; text-align: center;
    font-family: "Great Vibes", cursive; font-size: 34px; color: var(--rose); font-weight: 400;
  }
  .copy { position: absolute; left: 22px; right: 22px; font-size: 15.5px; line-height: 1.2; font-weight: 600; color: var(--text); }
  .copy--intro { top: 325px; }
  .web-band {
    position: absolute; left: 0; right: 0; top: 405px; height: 40px;
    background: linear-gradient(90deg, var(--band), #f8dbe7 70%, transparent);
    text-align: center; line-height: 40px;
    font-size: 19px; font-weight: 700; color: var(--magenta);
  }
  .copy--forms { top: 470px; }
  .copy--email { top: 560px; }
  .copy--call { top: 628px; }

  /* Contact panel */
  .lily {
    position: absolute; left: 40px; top: 0; width: 260px; height: 260px;
    background: radial-gradient(ellipse at 50% 40%, rgba(240,190,210,.75) 0%, rgba(246,210,224,.45) 45%, rgba(251,236,242,0) 72%);
  }
  .wordmark {
    font-family: "Crimson Text", Georgia, serif; font-weight: 600; color: var(--magenta);
    display: flex; align-items: center; justify-content: center; gap: 10px; white-space: nowrap;
  }
  .wordmark__dot { width: 12px; height: 12px; border-radius: 50%; background: var(--rose); }
  .contact-logo { position: absolute; top: 60px; width: 100%; font-size: 36px; }
  .contact-title {
    position: absolute; top: 218px; width: 100%; text-align: center;
    font-family: "Great Vibes", cursive; font-size: 34px; color: var(--rose); font-weight: 400;
  }
  .contact-info { position: absolute; left: 24px; right: 20px; top: 290px; font-size: 15.5px; line-height: 1.2; font-weight: 600; color: var(--text); }
  .contact-info p { margin-bottom: 22px; }
  .map {
    position: absolute; left: 22px; top: 492px; width: 300px; height: 170px;
    border: 3px solid var(--map-frame);
    background: linear-gradient(135deg, #e6eadf 0%, #dfe3d8 50%, #ecece4 100%);
  }

  /* Cover panel */
  .cover-photo {
    position: absolute; left: 0; top: 0; width: 100%; height: 480px;
    background: radial-gradient(ellipse at 45% 45%, #e2a27c 0%, #d08a64 40%, #f6e6e4 80%, #fff 100%);
  }
  .cover-logo { position: absolute; top: 545px; width: 100%; font-size: 38px; }
  .cover-tagline {
    position: absolute; top: 600px; width: 100%; text-align: center;
    font-size: 22px; color: var(--rose); letter-spacing: .5px;
  }

  /* Detachable card */
  .tear-card {
    position: absolute; left: 60px; top: 768px; width: 360px; height: 112px;
    background: linear-gradient(180deg, var(--paper-light), var(--paper));
    box-shadow: 0 4px 10px rgba(0,0,0,.15);
  }
  .tear-card__logo { position: absolute; top: 22px; width: 100%; font-size: 32px; }
  .tear-card__cut { position: absolute; left: 14px; right: 14px; bottom: 18px; border-top: 2px dashed var(--magenta); }
</style>
</head>
<body>
  <main class="brochure">
    <section class="panel panel--doctor">
      <svg class="swoosh" style="top:0;height:290px" viewBox="0 0 360 290" preserveAspectRatio="none" aria-hidden="true">
        <path d="M0 20 C 30 150, 150 250, 360 200 L 360 215 C 150 270, 20 180, 0 60 Z" fill="var(--rose-soft)" opacity=".6"/>
        <path d="M10 0 C 40 140, 170 240, 360 190 L 360 198 C 170 250, 30 150, 0 10 Z" fill="var(--rose)" opacity=".7"/>
      </svg>
      <div class="doctor-photo" role="img" aria-label="Portrait photo of Dr. Lena Korwin"></div>
      <h2 class="doctor-name">Dr. Lena Korwin</h2>
      <p class="copy copy--intro">To learn more information about Dr. Korwin, the services we offer, important clinical information and all that you need to know concerning insurance and payment, please visit our website:</p>
      <div class="web-band">www.maplewoodsurgery.example</div>
      <p class="copy copy--forms">There, you can download any forms that will need to be printed and completed prior to your visit. There is also a great question-and-answer section which covers many common queries.</p>
      <p class="copy copy--email">Additionally, you can email Dr. Korwin directly - it's easy and confidential.</p>
      <p class="copy copy--call">To schedule an appointment, please call us at (555) 014-2052. We look forward to hearing from you soon and participating in your medical care.</p>
    </section>

    <section class="panel panel--contact">
      <div class="lily" role="img" aria-label="Soft pink lily flower decoration"></div>
      <div class="wordmark contact-logo"><span class="wordmark__dot"></span>Maplewood Surgery</div>
      <h2 class="contact-title">Contact Us</h2>
      <div class="contact-info">
        <p>We are located at the Breast Center inside the Harlan Whitcomb Cancer Center</p>
        <p>On the campus of Brookfield Hospital<br>1840 Linden Crest Dr, Suite 100 Oakhaven, IL 62099</p>
        <p>Phone: (555) 014-2052<br>Fax: (555) 014-6683</p>
      </div>
      <div class="map" role="img" aria-label="Street map showing the office location"></div>
    </section>

    <section class="panel panel--cover">
      <div class="cover-photo" role="img" aria-label="Photo of a woman's torso, arms covering her chest"></div>
      <svg class="swoosh" style="top:300px;height:230px" viewBox="0 0 360 230" preserveAspectRatio="none" aria-hidden="true">
        <path d="M0 20 C 40 170, 200 210, 360 110 L 360 230 L 0 230 Z" fill="#fbeaf1"/>
        <path d="M0 0 C 40 160, 200 200, 360 95 L 360 110 C 200 215, 40 180, 0 22 Z" fill="var(--magenta)"/>
        <path d="M0 30 C 50 180, 210 215, 360 125 L 360 133 C 210 225, 45 190, 0 45 Z" fill="var(--rose)" opacity=".8"/>
        <path d="M0 55 C 60 195, 220 225, 360 145 L 360 150 C 220 232, 55 205, 0 65 Z" fill="var(--rose-soft)" opacity=".7"/>
      </svg>
      <div class="wordmark cover-logo"><span class="wordmark__dot"></span>Maplewood Surgery</div>
      <p class="cover-tagline">Comprehensive Breast Care</p>
    </section>
  </main>

  <aside class="tear-card">
    <div class="wordmark tear-card__logo"><span class="wordmark__dot"></span>Maplewood Surgery</div>
    <div class="tear-card__cut"></div>
  </aside>
</body>
</html>
```